Corporate Brochure Design

Hi there.

I need an A4 double sided brochure that would compliment our existing web site design and logo at www.keelhavenmetrics.com.

This brochure will be used as both a printed brochure and a PDF.

I would like the final design files to include a MS Word document template as we dont use any graphic design apps like adobe photoshop or illustrator.

I want to be able to easily produce industry specific versions of the brochure by swapping the image (or images) and changing the title and introductory paragraph of text.

The front page will contain the main message (See below).
The back page will contain either
- a couple of brief case studies (half a page each which should include each company's logo) or
- one large case study or
- a page about some aspect of our software.

An example case study can be found at http://www.keelhavenmetrics.com/Customers/Pemberly-Outlook-Register.aspx

An example page about our software can be found at
http://www.keelhavenmetrics.com/Solutions/Assessments-and-Benchmarking.aspx

I've included 2 testimonials to include. Please use them either in their entirety or cut down if required for space reasons.

Regarding images, i'm open to adopting a common theme of images from a single designer (and may even apply them to the website also) but please bear in mind the need to easily swap images to suite different industry audiences as mentioned above.

I'm not sure what the process is regarding stock photos here on ArtPorchly. But if you supply the product code I will purchase them as required. I tend to steer away from PicVault because their prices are quite high. But if you must use picvault then so be it.

Thank you! Content for the front page follows and the logo is attached. Let me know if you need anything else. Cheers.
--------------------------------------------------
Let Us Take Care of Your Carbon Reporting Needs

Do is it feel like a never-ending challenge to continually collate your carbon footprint report? Is it often someone different who ends up with the task and thus lacks the experience to move the business forward on the topic? Are there delays in the availability of data during busy reporting months? Do you wish that someone else could just take care of it all, leaving you to focus on your business?

KeelhavenGlimpse is a complete service where we take care of everything. From collating your data and calculating your emissions to analysing the results and reporting the figures and findings. We will chase your suppliers for your data, analyse the trends and produce a complete report suitable for stakeholders and executives. We can even develop a strategy for your business to reduce your carbon footprint.

And you’ll find our service is very competitively priced. Why? Because behind the scenes is a high degree of automation by our online KeelhavenMetrics™ software. KeelhavenMetrics™ is used by businesses around the world to manage their carbon and sustainability reporting processes. This is what we do and we’re good at it.

Our experienced advisors ensure you’re reporting an accurate picture to your stakeholders. A picture that is backed by rigorous processes and can be audited by a third party if necessary.

We can show you where and how to reduce your carbon emissions and actually save money. Your stakeholders will be reassured that your business has a “green” plan and is taking action.

The KeelhavenGlimpse service includes:

- Collecting your data – We’ll collect your data from your suppliers and accounts people. We’ll even chase them up if needed
- Calculating your emissions – We’ll ensure the correct emission factors are used and the data and calculations are auditable
- Analysing your trends – We’ll highlight to you the key trends in your emissions and suggest reasons for them
- Reporting the figures and findings – We’ll produce a complete report in Microsoft Word or PDF that you can give to your stakeholders, executives and auditors

Find out more about KeelhavenGlimpse at www.keelhavenmetrics.com/glimpse

Contact Us:
Call: +64 9 471 8605
Email: glimpse@keelhavenmetrics.com

We can also help with:
- half year or quarterly progress reports
- carbon reduction strategies
- end of year reporting
- executive summary and dashboard

(Testimonials)
“When we implemented KeelhavenMetrics™ at Torrow Mutual Trust we had previously relied on a spreadsheet process. This meant that information and data was unreliable and could rarely be traced. KeelhavenMetrics™ gave us rigour and reliability around our carbon footprint processes. Reporting twice yearly went from being a 4 month process to a 4 week process!” Dennis Carrow, Consultant.

“As an auditor, KeelhavenMetrics™ makes my job so much easier. From high level reports to low level detail, I can see where every piece of data came from. Along the way I can see the who, what, why and when, all tracing back to the original data file that was uploaded by the supplier. Everything is there in one place.” Anton Pirelli, Senior Consultant, Marsham.

Target Market(s)

Corporates, multi-nationals, mid sized companies. Clients include banks and financial institutions, retailers, engineering companies, major cities and universities.

Requirements
Must have
• Be professional, corporate but inspiring. Pictures say a 1000 words. I like positive pictures to do with sustainability, environment, corporate social responsibility, transparency in reporting. But nothing cliche.

```html
<!DOCTYPE html>
<html lang="en">
<head>
<meta charset="utf-8">
<title>KeelhavenGlimpse Brochure</title>
<link href="https://fonts.googleapis.com/css2?family=Oswald:wght@400;500&family=Open+Sans:wght@400;600&display=swap" rel="stylesheet">
<style>
  :root {
    --stage: #d6d6d6;
    --paper: #ffffff;
    --ink: #3a3a3a;
    --muted: #6b6b6b;
    --red: #d7282f;
    --blue: #2f6fc0;
    --navy: #0f2a44;
    --dark: #161616;
    --logo-grey: #7a7f86;
  }
  * { box-sizing: border-box; margin: 0; padding: 0; }
  html, body { width: 1200px; height: 1200px; overflow: hidden; }
  body {
    background: radial-gradient(circle at 50% 45%, #f2f2f2 0%, var(--stage) 70%, #bdbdbd 100%);
    font-family: "Open Sans", sans-serif;
    color: var(--ink);
    position: relative;
  }
  .sheet {
    position: absolute;
    top: 218px;
    width: 540px;
    height: 764px;
    background: var(--paper);
    box-shadow: 0 10px 30px rgba(0,0,0,.25);
    overflow: hidden;
  }
  .sheet--front { left: 50px; }
  .sheet--back { left: 610px; }
  .abs { position: absolute; }

  /* front */
  .brand { left: 28px; top: 22px; display: flex; align-items: center; gap: 8px; }
  .brand__dot { width: 22px; height: 22px; border-radius: 50%; background: var(--red); }
  .brand__name { font-family: "Oswald", sans-serif; font-weight: 400; font-size: 26px; color: var(--logo-grey); letter-spacing: .5px; }
  .hero { left: 0; top: 66px; width: 540px; height: 190px; }
  .hero__photo { left: 210px; top: 82px; width: 330px; height: 160px;
    background: radial-gradient(circle at 55% 50%, #4d7a3a 0%, #2b3a2a 35%, #141414 75%); }
  .hero__title { left: 28px; top: 92px; font-family: "Oswald", sans-serif; font-weight: 500; font-size: 21px; line-height: 1.15; color: #fff; }
  .hero__title .accent { color: var(--red); }
  .phone { right: 30px; top: 112px; font-family: "Oswald", sans-serif; font-size: 19px; color: var(--red); }
  .intro { left: 28px; top: 270px; width: 484px; column-count: 2; column-gap: 20px; font-size: 7.2px; line-height: 1.45; color: var(--muted); }
  .intro p { margin-bottom: 5px; }
  .divider { left: 0; top: 418px; width: 540px; height: 40px; }
  .more { left: 28px; top: 452px; width: 240px; font-family: "Oswald", sans-serif; font-size: 10.5px; line-height: 1.35; z-index: 2; }
  .more__lead { color: var(--ink); }
  .more__contact { color: var(--red); margin-top: 6px; }
  .team-photo { left: 280px; top: 440px; width: 232px; height: 100px; background: linear-gradient(180deg, #f4f4f4, #cfd6de); }
  .globe { left: 34px; top: 572px; width: 116px; height: 116px; border-radius: 50%; background: radial-gradient(circle, #a9c27f 0%, #c9d8a8 70%, rgba(201,216,168,0) 72%); }
  .tablet-photo { left: 150px; top: 552px; width: 390px; height: 150px; background: linear-gradient(135deg, #9fd0f0 0%, #3d8ed0 55%, #274b78 100%); border-top-left-radius: 140px 60px; }
  .base { left: 0; bottom: 0; width: 540px; height: 70px; }

  /* back */
  .banner-photo { left: 0; top: 0; width: 540px; height: 200px; background: radial-gradient(ellipse at 55% 55%, #e08a3a 0%, #2a6a8c 30%, #0c2d44 70%, #071a2a 100%); }
  .banner-curve { left: 0; top: 140px; width: 540px; height: 70px; }
  .section-title { font-family: "Oswald", sans-serif; font-size: 15px; color: var(--red); }
  .help { left: 30px; top: 218px; width: 300px; }
  .help ul { margin-top: 5px; list-style: none; font-size: 8px; line-height: 1.6; color: var(--muted); }
  .help li::before { content: "– "; }
  .testimonials { left: 30px; top: 318px; width: 300px; }
  .quote { margin-top: 6px; font-size: 7.2px; line-height: 1.45; color: var(--muted); }
  .quote cite { display: block; font-style: normal; font-weight: 600; color: var(--ink); margin-top: 2px; }
  .globe--back { left: 300px; top: 420px; width: 210px; height: 190px; }
  .contact { left: 0; top: 612px; width: 540px; height: 152px; }
  .contact__text { left: 140px; top: 650px; width: 280px; text-align: center; font-family: "Oswald", sans-serif; }
  .contact__title { font-size: 20px; color: var(--red); }
  .contact__line { font-size: 12px; color: var(--red); line-height: 1.35; }
  .contact__web { font-size: 12px; color: var(--blue); }
</style>
</head>
<body>

<section class="sheet sheet--front" aria-label="Brochure front page">
  <div class="abs brand"><span class="brand__dot"></span><span class="brand__name">KeelhavenMetrics™</span></div>

  <svg class="abs hero" viewBox="0 0 540 190" aria-hidden="true">
    <path d="M0 18 Q270 -6 540 22 L540 176 Q270 150 0 178 Z" fill="#161616"/>
    <path d="M0 14 Q270 -10 540 18" stroke="#2f6fc0" stroke-width="4" fill="none"/>
    <path d="M0 184 Q270 156 540 182" stroke="#2f6fc0" stroke-width="4" fill="none"/>
  </svg>
  <div class="abs hero__photo" role="img" aria-label="Hands holding a glowing green sustainability graphic"></div>
  <h1 class="abs hero__title">Let Us Take Care of Your<br><span class="accent">Carbon Reporting</span><br>Needs</h1>
  <div class="abs phone">64 9 471 8605</div>

  <div class="abs intro">
    <p>Does it feel like a never-ending challenge to continually collate your carbon footprint report? Is it often someone different who ends up with the task and thus lacks the experience to move the business forward on the topic? Are there delays in the availability of data during busy reporting months? Do you wish that someone else could just take care of it all, leaving you to focus on your business?</p>
    <p>KeelhavenGlimpse is a complete service where we take care of everything. From collating your data and calculating your emissions to analysing the results and reporting the figures and findings. We will chase your suppliers for your data, analyse the trends and produce a complete report suitable for stakeholders and executives.</p>
    <p>And you’ll find our service is very competitively priced. Why? Because behind the scenes is a high degree of automation by our online KeelhavenMetrics™ software, used by businesses around the world to manage their carbon and sustainability reporting.</p>
    <p>Our experienced advisors ensure you’re reporting an accurate picture to your stakeholders. A picture that is backed by rigorous processes and can be audited by a third party if necessary. We can show you where and how to reduce your carbon emissions and actually save money.</p>
  </div>

  <svg class="abs divider" viewBox="0 0 540 40" aria-hidden="true">
    <path d="M0 30 Q270 0 540 26" stroke="#d7282f" stroke-width="3" fill="none"/>
  </svg>

  <div class="abs team-photo" role="img" aria-label="Smiling business team standing together"></div>
  <div class="abs globe" role="img" aria-label="Green globe illustration with eco icons"></div>
  <div class="abs tablet-photo" role="img" aria-label="Hand touching a tablet with a growing plant"></div>

  <div class="abs more">
    <p class="more__lead">Find out more about KeelhavenGlimpse<br>at www.keelhavenmetrics.com/glimpse</p>
    <p class="more__contact">Contact Us:<br>Call: +64 9 471 8605<br>Email: glimpse@keelhavenmetrics.com<br>www.keelhavenmetrics.com/glimpse</p>
  </div>

  <svg class="abs base" viewBox="0 0 540 70" aria-hidden="true">
    <path d="M0 40 Q270 10 540 36 L540 70 L0 70 Z" fill="#2f6fc0"/>
    <path d="M0 34 Q270 4 540 30" stroke="#d7282f" stroke-width="3" fill="none"/>
  </svg>
</section>

<section class="sheet sheet--back" aria-label="Brochure back page">
  <div class="abs banner-photo" role="img" aria-label="Night city skyline with glowing data lights"></div>
  <svg class="abs banner-curve" viewBox="0 0 540 70" aria-hidden="true">
    <path d="M0 60 Q270 20 540 50 L540 70 L0 70 Z" fill="#ffffff"/>
    <path d="M0 58 Q270 18 540 48" stroke="#2f6fc0" stroke-width="3" fill="none"/>
  </svg>

  <div class="abs help">
    <h2 class="section-title">We can also help with:</h2>
    <ul>
      <li>half year or quarterly progress reports</li>
      <li>carbon reduction strategies</li>
      <li>end of year reporting</li>
      <li>executive summary and dashboard</li>
    </ul>
  </div>

  <div class="abs testimonials">
    <h2 class="section-title">Testimonials</h2>
    <blockquote class="quote">“When we implemented KeelhavenMetrics™ at Torrow Mutual Trust we had previously relied on a spreadsheet process. KeelhavenMetrics™ gave us rigour and reliability around our carbon footprint processes. Reporting twice yearly went from being a 4 month process to a 4 week process!”<cite>Dennis Carrow, Consultant</cite></blockquote>
    <blockquote class="quote">“As an auditor, KeelhavenMetrics™ makes my job so much easier. From high level reports to low level detail, I can see where every piece of data came from. Everything is there in one place.”<cite>Anton Pirelli, Senior Consultant, Marsham</cite></blockquote>
  </div>

  <svg class="abs globe--back" viewBox="0 0 210 190" role="img" aria-label="Green globe illustration with city and wind turbine icons">
    <circle cx="105" cy="100" r="80" fill="#b4c98c" opacity=".75"/>
  </svg>

  <svg class="abs contact" viewBox="0 0 540 152" aria-hidden="true">
    <path d="M0 22 Q270 -8 540 20" stroke="#d7282f" stroke-width="3" fill="none"/>
    <path d="M0 30 Q270 0 540 28" stroke="#2f6fc0" stroke-width="3" fill="none"/>
    <path d="M0 132 Q270 108 540 128 L540 152 L0 152 Z" fill="#2f6fc0"/>
  </svg>
  <div class="abs contact__text">
    <h2 class="contact__title">Contact Us:</h2>
    <p class="contact__line">Call: +64 9 471 8605</p>
    <p class="contact__line">Email: glimpse@keelhavenmetrics.com</p>
    <p class="contact__web">www.keelhavenmetrics.com/glimpse</p>
  </div>
</section>

</body>
</html>
```